Flyer Needed to Advertise New Online Reading Programs

ABOUT THE ACADEMY OF LITERACY GROWTH
The Institute teaches summer reading skills programs for elementary school students, in programs offered through partnerships with universities, colleges and municipalities nationwide. The goal of each program is to build reading skills, and to foster a lifetime love of books and reading.

AIMS & TARGET MARKET
The Institute has developed a new format of its’ online reading program for elementary students, which includes live small-group video classes taught by a professional reading teacher. The Institute seeks a new graphic design for a flyer to advertise the new online reading program. The flyer will be sent to elementary schools, passed out by teachers, and then taken home by students to show parents; therefore, the primary audience for the flyer will be teachers and parents of elementary school students.

Live classes for children are completely new in online education, unlike anything else in the marketplace, and parents and teachers therefore have no experience with them. The successful design will include illustrations or photographs that allow visitors to immediately grasp/understand the new video class format, without relying heavily on a written description. Additionally, the successful flyer concept will make the program, and the video classes in particular, feel fun and appealing to kids and parents.

Below is additional information about the new live small-group video class format, which meets weekly for 6 weeks:
o During video classes, students participate from home.
o During discussions, the student’s computer (or tablet) screen is filled with live video frames of the teacher and the other students. The video frame for the teacher is larger, and the other students appear in smaller frames.
o During other video class instruction, the teacher uses a presentation screen to display pages of a book or a “whiteboard” used for instructional activities.

Notes: The flyer design could include an illustrated or photo screenshot of a video class, with children looking engaged and a teacher leading them in discussion (stock photos are okay to use in flyer design). We have included a screen shot of one of these classes for reference, but do not feel constrained to represent this screen realistically (as shown here). Layout, look and feel can be changed. Alternatively, you may choose to use a graphic other than a screenshot to bring across the concept of the video classes.

COPY AND SPECIFICATIONS
The flyer design will be one-sided and the dimensions are 8.5” x 11” in either portrait or landscape orientation. We will consider designs in color or black and white. Since we brand our flyers with logos of the universities we partner with throughout the nation, we’ll need to include a partner logo in the design. Exact copy will be provided, but layout is flexible. Screenshots from our sample classes are included to show screen layout. Stock photos are okay to use in flyer designs.

Hi designers, We wanted to share our thoughts on the main image of the flyer. We're leaning towards an image that shows a sole student on a computer with the computer screen in view. The computer screen could have the sample image we provided to show how the video classes operate. Thanks! The Academy of Literacy Growth

```html
<!DOCTYPE html>
<html lang="en">
<head>
<meta charset="utf-8">
<title>Reading Skills Classes – Online this Summer</title>
<link href="https://fonts.googleapis.com/css2?family=Mulish:wght@400;600;800&family=Roboto+Condensed:wght@400&display=swap" rel="stylesheet">
<style>
  :root {
    --backdrop: #b3b2b0;
    --paper: #ffffff;
    --hero-tint: #e4e2dd;
    --brand-blue: #1a8ed6;
    --heading-blue: #1d86cc;
    --band-dark: #1f1d1e;
    --ink: #2b2b2b;
    --ink-soft: #3d3d3d;
    --white: #ffffff;
  }
  * { box-sizing: border-box; margin: 0; padding: 0; }
  html, body { width: 1200px; height: 1200px; overflow: hidden; }
  body { background: var(--backdrop); font-family: "Mulish", sans-serif; color: var(--ink); }

  .flyer {
    position: absolute; left: 162px; top: 33px;
    width: 876px; height: 1134px;
    background: var(--paper);
    overflow: hidden;
  }

  /* Hero */
  .hero { position: absolute; left: 0; top: 0; width: 876px; height: 420px; background: var(--hero-tint); }
  .hero-photo {
    position: absolute; left: 330px; top: 0; width: 546px; height: 420px;
    background:
      linear-gradient(90deg, var(--hero-tint) 0%, rgba(228,226,221,0) 22%),
      linear-gradient(180deg, #e9e6df 0%, #d8d3c8 45%, #c9b9a3 70%, #bfb3a6 100%);
  }
  .hero-photo::after {
    content: ""; position: absolute; right: 0; top: 0; width: 140px; height: 420px;
    background: linear-gradient(90deg, rgba(200,160,110,0) 0%, rgba(196,150,100,0.55) 100%);
  }
  .title-box {
    position: absolute; left: 40px; top: 72px; height: 58px; padding: 0 26px 0 22px;
    background: var(--brand-blue); color: var(--white);
    display: flex; align-items: center;
    font-size: 29px; letter-spacing: 0.5px; font-weight: 400;
  }
  .title-box strong { font-weight: 800; margin-right: 8px; }
  .subtitle-box {
    position: absolute; left: 40px; top: 134px; width: 287px; height: 48px;
    background: var(--brand-blue); color: var(--white);
    display: flex; align-items: center; padding-left: 20px;
    font-size: 24px; font-weight: 400;
  }
  .feature-list {
    position: absolute; left: 40px; top: 230px; width: 300px;
    list-style: none; font-size: 19px; line-height: 24px; color: var(--ink-soft);
  }
  .feature-list li { position: relative; padding-left: 18px; margin-bottom: 3px; }
  .feature-list li::before { content: "•"; position: absolute; left: 0; }

  /* Skills band */
  .skills-band {
    position: absolute; left: 0; top: 420px; width: 876px; height: 110px;
    background: var(--band-dark); color: var(--white);
  }
  .skills-col { position: absolute; top: 26px; list-style: none; font-size: 19px; line-height: 29px; }
  .skills-col li { position: relative; padding-left: 18px; }
  .skills-col li::before { content: "•"; position: absolute; left: 0; }
  .skills-col.first { left: 40px; }
  .skills-col.second { left: 198px; }
  .skills-col.third { left: 409px; }
  .partner-name {
    position: absolute; left: 686px; top: 26px; width: 148px; height: 62px;
    border: 1px solid var(--white);
    display: flex; flex-direction: column; align-items: center; justify-content: center;
    font-size: 15px; font-weight: 600; letter-spacing: 1.5px; line-height: 20px;
  }

  /* Programs */
  .program { position: absolute; width: 375px; }
  .program h2 {
    font-family: "Roboto Condensed", sans-serif; font-weight: 400;
    font-size: 16px; color: var(--heading-blue); text-transform: uppercase;
    line-height: 20px; margin-bottom: 8px;
  }
  .program p { font-size: 13.5px; line-height: 17.4px; text-align: justify; color: var(--ink); }
  .col-left { left: 40px; }
  .col-right { left: 462px; }
  .row-1 { top: 564px; }
  .row-2 { top: 682px; }
  .row-3 { top: 806px; }
  .row-4 { top: 946px; }

  /* Call to action */
  .cta {
    position: absolute; left: 462px; top: 945px; width: 372px; height: 151px;
    background: var(--brand-blue); color: var(--white); text-align: center;
    padding-top: 22px;
  }
  .cta-lead { font-size: 18px; }
  .cta-phone { font-size: 27px; font-weight: 800; margin-top: 8px; letter-spacing: 0.3px; }
  .cta-hours { font-size: 13.5px; line-height: 17px; margin-top: 12px; }
</style>
</head>
<body>
  <main class="flyer">
    <section class="hero">
      <div class="hero-photo" role="img" aria-label="Photo of a young girl at a desktop computer joining a live video reading class, with her mother watching beside her in a bright room"></div>
      <h1 class="title-box"><strong>READING</strong> SKILLS CLASSES</h1>
      <div class="subtitle-box">Online this Summer!</div>
      <ul class="feature-list">
        <li>Small class size</li>
        <li>A skilled and encouraging teacher</li>
        <li>Individualized skills instruction</li>
        <li>A program of independent reading in great books</li>
      </ul>
    </section>

    <section class="skills-band">
      <ul class="skills-col first"><li>Phonics</li><li>Study Skills</li></ul>
      <ul class="skills-col second"><li>Comprehension</li><li>Speed Reading</li></ul>
      <ul class="skills-col third"><li>Fluency</li><li>Love of Reading</li></ul>
      <div class="partner-name"><span>HARBORVIEW</span><span>UNIVERSITY</span></div>
    </section>

    <article class="program col-left row-1">
      <h2>Program for Preschoolers:</h2>
      <p>Students in this program build strong reading readiness skills. Your child will learn letter recognition and beginning phonics, and develop the motivation and love of reading that make learning to read easy, enjoyable, and successful.</p>
    </article>
    <article class="program col-right row-1">
      <h2>Program for Entering Kindergartners:</h2>
      <p>Students in this program learn beginning reading skills and develop a love of books. Your child will learn letter recognition, phonics, and sight words, and will learn to sound out short words.</p>
    </article>
    <article class="program col-left row-2">
      <h2>Program for Entering 1st Graders:</h2>
      <p>Students in this program learn to read independently. Your child will learn phonics and sight words, build comprehension, and gain the skills and confidence needed for success in first grade.</p>
    </article>
    <article class="program col-right row-2">
      <h2>Program for Entering 2nd Graders:</h2>
      <p>Students in this program become fluent, independent readers. Your child will make significant gains in phonics and word-attack skills, fluency, and comprehension, and will develop confidence and a love of reading.</p>
    </article>
    <article class="program col-left row-3">
      <h2>Program for Entering 3rd Graders:</h2>
      <p>Students in this program become strong independent readers. Your child will develop the comprehension, fluency, and long-word decoding skills needed to read longer books with ease, and will build confidence and a love of reading.</p>
    </article>
    <article class="program col-right row-3">
      <h2>Program for Entering 4th and 5th Graders:</h2>
      <p>Students in this program make substantial gains in comprehension, long-word decoding skills, fluency, and reading speed. Your child will complete homework more quickly and easily, be more successful in school, and become a strong, enthusiastic reader.</p>
    </article>
    <article class="program col-left row-4">
      <h2>Programs for Entering 6th-8th Graders and Entering 9th and 10th Graders:</h2>
      <p>Students in these programs make substantial gains in comprehension while doubling reading speed. They also learn the best way to read textbooks, take notes, and study for tests. As a result, students complete homework more quickly and easily, get better grades, and enjoy reading more.</p>
    </article>

    <aside class="cta">
      <p class="cta-lead">For More Information or to Register</p>
      <p class="cta-phone">Call 1-800-555-0147</p>
      <p class="cta-hours">Mon.–Fri.&nbsp;&nbsp;&nbsp;&nbsp;5am–7pm<br>Sat.&nbsp; 5am–4pm&nbsp;&nbsp; |&nbsp;&nbsp; Sun.&nbsp; 6am–4pm</p>
    </aside>
  </main>
</body>
</html>
```